Borrowdale Equity Business Card

Looking for a design for our business cards. Need to look corporate and outstanding. I have enclosed our logos for the company. Borrowdale equity is an investment firm for high level clients looking for advisory in their investments. White background or black is good. We will like to double sided options maybe at the back with just the logo of the firm.

Example of the info for the business card:

Marcus Heller
Managing Director

Panama Phone +507 391 4786
Switzerland Phone +41 43 917 2648
test@borrowdale-equity-example.com
www.borrowdale-equity-example.com

Industry/Entity Type

Investment

```html
<!DOCTYPE html>
<html lang="en">
<head>
<meta charset="utf-8">
<title>Borrowdale Equity – Business Card</title>
<link rel="stylesheet" href="https://fonts.googleapis.com/css2?family=Exo+2:wght@400;500;600&display=swap">
<style>
  :root {
    --stage: #6c6f77;
    --card-white: #ffffff;
    --navy: #223e8c;
    --navy-deep: #1c3170;
    --navy-shade: #263a6e;
    --panel-grey: #e5e8f0;
    --ink: #27335a;
    --gold: #b88a2a;
  }
  * { box-sizing: border-box; margin: 0; padding: 0; }
  html, body {
    width: 1200px; height: 1082px; overflow: hidden;
    background: var(--stage);
  }
  .canvas {
    position: relative; width: 1200px; height: 1082px;
    display: flex; align-items: center; justify-content: center;
  }
  .card {
    position: relative; width: 1000px; height: 572px;
    background: var(--card-white); overflow: hidden;
    box-shadow: 0 10px 30px rgba(0,0,0,.25);
    font-family: "Exo 2", sans-serif;
  }
  .card-shapes { position: absolute; inset: 0; width: 100%; height: 100%; }
  .name-line {
    position: absolute; left: 330px; top: 118px;
    color: #fff; font-size: 30px; letter-spacing: 2px; font-weight: 500;
    display: flex; align-items: center; gap: 16px; text-transform: uppercase;
    white-space: nowrap;
  }
  .name-line .divider { font-size: 34px; font-weight: 400; }
  .name-line .role { font-size: 19px; letter-spacing: 2.5px; font-weight: 400; }
  .brand {
    position: absolute; left: 440px; top: 274px;
    display: flex; align-items: center; gap: 18px; white-space: nowrap;
  }
  .brand-mark { width: 24px; height: 24px; background: var(--gold); flex: none; }
  .brand-name {
    font-family: "Exo 2", sans-serif; font-weight: 500;
    font-size: 34px; letter-spacing: 3px; color: var(--navy);
    text-transform: uppercase;
  }
  .contact-list {
    position: absolute; left: 48px; top: 218px; width: 340px;
    list-style: none; color: var(--ink); font-size: 15px; letter-spacing: .3px;
    display: flex; flex-direction: column; gap: 14px;
  }
  .contact-list li { display: flex; align-items: center; gap: 11px; white-space: nowrap; }
  .contact-list svg { width: 16px; height: 16px; flex: none; }
  .address {
    position: absolute; right: 40px; top: 438px;
    color: #fff; font-size: 22px; letter-spacing: 1.5px; font-weight: 400;
    white-space: nowrap;
  }
</style>
</head>
<body>
<main class="canvas">
  <section class="card" aria-label="Business card front">
    <svg class="card-shapes" viewBox="0 0 1000 572" preserveAspectRatio="none" aria-hidden="true">
      <rect class="band-top" x="0" y="0" width="1000" height="180" fill="var(--navy)"/>
      <rect class="contact-panel" x="0" y="180" width="400" height="232" fill="var(--panel-grey)"/>
      <rect class="band-bottom" x="0" y="412" width="1000" height="160" fill="var(--navy)"/>
      <polygon class="accent-top" points="0,0 150,0 250,180 0,180" fill="var(--navy-shade)" opacity=".85"/>
      <polygon class="accent-side" points="0,180 36,180 0,280" fill="var(--navy-shade)" opacity=".3"/>
      <polygon class="accent-bottom" points="0,572 0,412 420,412 240,572" fill="var(--navy-deep)" opacity=".8"/>
    </svg>

    <div class="name-line">
      <span class="name">Marcus Heller</span>
      <span class="divider">|</span>
      <span class="role">Managing Director</span>
    </div>

    <div class="brand">
      <span class="brand-mark"></span>
      <span class="brand-name">Borrowdale Equity</span>
    </div>

    <ul class="contact-list">
      <li>
        <svg viewBox="0 0 24 24"><path fill="var(--ink)" d="M6.6 10.8a15 15 0 0 0 6.6 6.6l2.2-2.2c.3-.3.7-.4 1-.2 1.1.4 2.3.6 3.6.6.6 0 1 .4 1 1V20c0 .6-.4 1-1 1A17 17 0 0 1 3 4c0-.6.4-1 1-1h3.5c.6 0 1 .4 1 1 0 1.3.2 2.5.6 3.6.1.3 0 .7-.2 1z"/></svg>
        <span>+507 391 4786</span>
      </li>
      <li>
        <svg viewBox="0 0 24 24"><rect x="6" y="2" width="12" height="20" rx="2" fill="none" stroke="var(--ink)" stroke-width="2"/><circle cx="12" cy="18" r="1.2" fill="var(--ink)"/></svg>
        <span>+41 43 917 2648</span>
      </li>
      <li>
        <svg viewBox="0 0 24 24"><rect x="2" y="5" width="20" height="14" rx="1.5" fill="var(--ink)"/><path d="M3 6l9 7 9-7" fill="none" stroke="#fff" stroke-width="1.6"/></svg>
        <span>test@borrowdale-equity-example.com</span>
      </li>
      <li>
        <svg viewBox="0 0 24 24"><circle cx="12" cy="12" r="10" fill="none" stroke="var(--ink)" stroke-width="2"/><path d="M2 12h20M12 2c3 3 3 17 0 20M12 2c-3 3-3 17 0 20" fill="none" stroke="var(--ink)" stroke-width="1.6"/></svg>
        <span>www.borrowdale-equity-example.com</span>
      </li>
    </ul>

    <p class="address">214 Harbour Lane, 3rd Floor, Suite W.</p>
  </section>
</main>
</body>
</html>
```